Business Card Design Project

use presentation folder design and my logo and make 4 over 4 business cards

Industry/Entity Type

Business

Requirements
Must have
• use the design from my presentation folder and put my logo on it

Name
Title
phone
fax
email

```html
<!DOCTYPE html>
<html lang="en">
<head>
<meta charset="utf-8">
<title>Kindpath Counseling – Business Cards</title>
<link rel="stylesheet" href="https://fonts.googleapis.com/css2?family=Comfortaa:wght@600&family=Old+Standard+TT:wght@400;700&display=swap">
<style>
  :root {
    --stage: #2e2e2e;
    --card-white: #f7f6f4;
    --cream: #f1ebe4;
    --panel-beige: #cfc6b8;
    --panel-beige-light: #e2dbd0;
    --soft-grey: #e4e4e4;
    --coffee: #6b4323;
    --gold: #a8861c;
    --ink: #2b2b2b;
    --ink-soft: #4a4a4a;
  }
  * { margin: 0; padding: 0; box-sizing: border-box; }
  html, body {
    width: 1200px; height: 900px; overflow: hidden;
    background: var(--stage);
  }
  .sheet {
    width: 1200px; height: 900px;
    display: flex; flex-direction: column; align-items: center; justify-content: center;
    gap: 36px;
  }
  .card {
    position: relative;
    width: 700px; height: 400px;
    overflow: hidden;
    box-shadow: 0 10px 30px rgba(0,0,0,.45);
  }
  .card-art { position: absolute; inset: 0; }

  /* contact side */
  .card--contact { background: var(--card-white); }
  .contact-brand {
    position: absolute; left: 165px; top: 70px;
    display: flex; align-items: center; gap: 10px;
    font-family: "Comfortaa", sans-serif; font-weight: 600;
    font-size: 22px; color: var(--gold);
  }
  .brand-dot {
    width: 14px; height: 14px; border-radius: 50%; background: var(--gold);
  }
  .contact-block {
    position: absolute; left: 365px; top: 120px;
    font-family: "Old Standard TT", serif; color: var(--ink);
  }
  .person-name { font-size: 27px; font-weight: 400; letter-spacing: 1px; text-transform: uppercase; }
  .person-title { font-size: 15px; color: var(--ink-soft); margin-top: 2px; }
  .contact-list { list-style: none; margin-top: 26px; font-size: 15px; line-height: 1.45; }
  .contact-list b { display: inline-block; width: 22px; color: var(--coffee); font-weight: 700; }

  /* logo side */
  .card--front { background: linear-gradient(135deg, var(--cream), var(--card-white) 70%); }
  .front-lockup {
    position: absolute; left: 0; right: 0; top: 150px;
    display: flex; flex-direction: column; align-items: center;
  }
  .front-name {
    display: flex; align-items: center; gap: 14px;
    font-family: "Comfortaa", sans-serif; font-weight: 600;
    font-size: 44px; color: var(--gold); line-height: 1.1; white-space: nowrap;
  }
  .front-name .brand-dot { width: 22px; height: 22px; }
  .front-tagline {
    font-family: "Old Standard TT", serif; font-size: 20px;
    letter-spacing: 2px; color: var(--coffee); margin-top: 18px;
  }
</style>
</head>
<body>
<main class="sheet">

  <section class="card card--contact" aria-label="Business card, contact side">
    <svg class="card-art" viewBox="0 0 700 400" aria-hidden="true">
      <path d="M0 0 H180 Q120 20 80 60 L0 80 Z" fill="var(--soft-grey)"/>
      <path d="M170 20 H700 V400 H380 L200 330 Q150 310 150 260 V70 Q150 20 200 20 Z" fill="var(--panel-beige)"/>
      <path d="M170 20 H700 V140 Q420 90 150 140 V70 Q150 20 200 20 Z" fill="var(--panel-beige-light)" opacity=".55"/>
      <path d="M0 210 L130 210 L330 300 Q360 315 340 345 L300 400 H0 Z" fill="var(--coffee)"/>
    </svg>
    <div class="contact-brand"><span class="brand-dot"></span>Kindpath</div>
    <div class="contact-block">
      <h1 class="person-name">Daniel Harlow</h1>
      <p class="person-title">Operation Manager</p>
      <ul class="contact-list">
        <li><b>T</b>(221) 555 0142</li>
        <li><b>F</b>(221) 555 0187</li>
        <li><b>E</b>daniel@kindpath.org</li>
      </ul>
    </div>
  </section>

  <section class="card card--front" aria-label="Business card, logo side">
    <div class="front-lockup">
      <p class="front-name"><span class="brand-dot"></span>Kindpath Counseling</p>
      <p class="front-tagline">steady support for recovery</p>
    </div>
  </section>

</main>
</body>
</html>
```